Successfully Managing through a Hurricane Training Event

This learning event is specifically for Birch Supply retailers/stores located outside of the US who are seeking guidance and help with how to plan, prepare, manage there business during Hurricane/Tropical Storm season.

----------------------------------------------
Event Title: Successfully Managing Through Hurricane Season

Event Description: Hurricanes and severe tropical storms are some of the most devastating, and costly, natural disasters known to humans. In fact, historically, 40% of small businesses impacted by a natural disaster do not reopen. If your business is vulnerable to these potential catastrophic events, it is important to develop an effective preparedness and mitigation plan, and take prompt action. Doing so will not only increase the safety of your store associates and customers, but it will help you remain in business after a hurricane strikes, improving your community’s ability to recover. This session focuses on:

o In-store preparation functions
o Implementing business continuity operating procedures for protecting and maintaining your business
o Sustaining the capability to provide products to customers
o Building a hurricane-ready optimized assortment of in-demand products, including special merchandising opportunities
o Deploying effective inventory management and system strategies for staying in stock
o Knowing your available contacts and rules of engagement
o Preserving a competitive advantage and reputation
o Optimizing the means by which you leverage your freight forwarding facility

Event is hosted by: Birch Worldwide Solutions www.birchworldservicesgroup.example

Logistical Details:
• Length: 1 hour
• Date: Friday, August 17, 2018
• Time: 1:00 – 2:00 p.m.

To Register for this Event, Go To: https://www.tovrelin.example/bir18/fall/

Pricing: $ 25 per participant
*Charged to Invoice post-show

Questions? For more information, contact Martin Olsby
+1 555-014-2836
molsby@birchsupply.example

Target Market(s)

Birch Supply International Stores

Industry/Entity Type

Retail

Font styles to use
Serif

Requirements
Must have
• See Word File Attachment
• Use Birch Supply red and black logo colors.
• 1 -Sided brochure
Nice to have
Should not have
• N/A

```html
<!DOCTYPE html>
<html lang="en">
<head>
<meta charset="utf-8">
<title>Successfully Managing Through Hurricane Season</title>
<link rel="stylesheet" href="https://fonts.googleapis.com/css2?family=Lato:wght@400;700;900&display=swap">
<style>
  :root {
    --red: #e31e24;
    --red-dark: #a8121a;
    --ink: #2a2a2a;
    --grey-text: #3d3d3d;
    --stage: #9c9c9c;
    --white: #ffffff;
    --storm-1: #3f5a5c;
    --storm-2: #9fb0b3;
  }
  * { margin: 0; padding: 0; box-sizing: border-box; }
  html, body { width: 722px; height: 1200px; overflow: hidden; background: var(--stage); }
  body { position: relative; font-family: "Lato", sans-serif; color: var(--ink); }

  .flyer {
    position: absolute; left: 16px; top: 113px;
    width: 468px; height: 660px;
    background: var(--white);
    transform: scale(1.4744); transform-origin: 0 0;
    overflow: hidden;
    box-shadow: 0 2px 6px rgba(0,0,0,.35);
  }
  .abs { position: absolute; }
  .hero, .footer-band { position: absolute; left: 0; width: 468px; }
  .hero { top: 0; height: 265px; }
  .footer-band { top: 460px; height: 200px; }

  .brand { left: 22px; top: 224px; display: flex; align-items: center; gap: 6px; }
  .brand-dot { width: 26px; height: 26px; border-radius: 50%; background: var(--red); }
  .brand-name { font-size: 13px; font-weight: 700; color: var(--ink); }

  .title { left: 22px; top: 268px; font-size: 17.5px; font-weight: 900; color: var(--red); line-height: 20px; text-transform: uppercase; }
  .heading { font-size: 10px; font-weight: 700; color: var(--red); text-decoration: underline; }
  .desc-head { left: 22px; top: 317px; }
  .desc { left: 22px; top: 334px; width: 424px; font-size: 8.1px; line-height: 11px; text-align: justify; color: var(--grey-text); }
  .focus-head { left: 22px; top: 410px; }

  .focus-list { list-style: none; font-size: 6.4px; line-height: 7.8px; color: var(--grey-text); }
  .focus-list li { position: relative; padding-left: 10px; margin-bottom: 4px; }
  .focus-list li::before { content: ""; position: absolute; left: 0; top: 2px; width: 3.5px; height: 3.5px; border-radius: 50%; background: var(--red); }
  .col-left { left: 35px; top: 431px; width: 170px; }
  .col-right { left: 236px; top: 431px; width: 215px; }

  .pricing {
    left: 62px; top: 514px; width: 138px; height: 60px;
    border: 1.5px solid var(--white); border-radius: 6px;
    background: linear-gradient(#3a3a3a, #050505);
    color: var(--white); text-align: center; padding-top: 6px;
  }
  .pricing-label { font-size: 11.5px; text-decoration: underline; }
  .pricing-amount { font-size: 9.5px; font-weight: 700; margin-top: 4px; }
  .pricing-note { font-size: 5px; margin-top: 3px; }

  .date-pill {
    left: 245px; top: 522px; width: 184px; height: 33px;
    border-radius: 17px; background: linear-gradient(#e1262c, #9e1016);
    box-shadow: 0 2px 3px rgba(0,0,0,.3);
    color: var(--white); font-weight: 700; font-size: 9.5px; line-height: 11px;
    text-align: center; padding-top: 5.5px;
  }

  .white { color: var(--white); }
  .footer-brand { left: 16px; top: 585px; display: flex; align-items: center; gap: 4px; }
  .footer-brand .brand-dot { width: 13px; height: 13px; background: var(--white); }
  .footer-brand .brand-name { font-size: 7.5px; color: var(--white); }
  .host { left: 17px; top: 609px; font-size: 7.6px; line-height: 12px; }

  .questions { left: 226px; top: 577px; font-size: 7.8px; }
  .contact { left: 279px; top: 589px; font-size: 8.2px; }
  .contact strong { font-weight: 700; }
  .contact-line { left: 278px; display: flex; align-items: center; gap: 8px; }
  .phone { top: 603px; font-size: 12px; font-weight: 700; }
  .email { top: 622px; font-size: 7.5px; }
  .web { top: 637px; font-size: 7.5px; }
  .icon { width: 10px; height: 10px; flex: none; }
</style>
</head>
<body>
  <main class="flyer">
    <svg class="hero" viewBox="0 0 468 265" aria-hidden="false">
      <defs>
        <linearGradient id="storm" x1="0" y1="0" x2="0" y2="1">
          <stop offset="0" stop-color="var(--storm-2)"/>
          <stop offset="1" stop-color="var(--storm-1)"/>
        </linearGradient>
      </defs>
      <path role="img" aria-label="Hurricane winds bending palm trees as waves crash against a beach house" d="M0 0 H468 V168 Q250 232 0 118 Z" fill="url(#storm)"/>
      <path d="M0 124 Q230 232 468 170 L468 226 Q270 268 40 160 Q18 146 0 136 Z" fill="var(--red)"/>
      <path d="M0 120 Q230 226 468 166 L468 176 Q230 236 0 130 Z" fill="var(--red-dark)"/>
    </svg>

    <div class="abs brand">
      <span class="brand-dot"></span>
      <span class="brand-name">Birch Worldwide Solutions</span>
    </div>

    <h1 class="abs title">Successfully Managing<br>Through Hurricane Season</h1>

    <h2 class="abs heading desc-head">Event Description:</h2>
    <p class="abs desc">Hurricanes and severe tropical storms are some of the most devastating, and costly, natural disasters known to humans. In fact, historically, 40% of small businesses impacted by a natural disaster do not reopen. If your business is vulnerable to these potential catastrophic events, it is important to develop an effective preparedness and mitigation plan, and take prompt action. Doing so will not only increase the safety of your store associates and customers, but it will help you remain in business after a hurricane strikes, improving your community’s ability to recover.</p>

    <h2 class="abs heading focus-head">This session focuses on:</h2>
    <ul class="abs focus-list col-left">
      <li>In-store preparation functions</li>
      <li>Sustaining the capability to provide products to customers</li>
      <li>Deploying effective inventory management and system strategies for staying in stock</li>
      <li>Optimizing the means by which you leverage your freight forwarding facility</li>
    </ul>
    <ul class="abs focus-list col-right">
      <li>Implementing business continuity operating procedures for protecting and maintaining your business</li>
      <li>Building a hurricane-ready optimized assortment of in-demand products, including special merchandising opportunities</li>
      <li>Knowing your available contacts and rules of engagement</li>
      <li>Preserving a competitive advantage and reputation</li>
    </ul>

    <svg class="footer-band" viewBox="0 0 468 200" aria-hidden="true">
      <path d="M0 92 Q120 70 250 80 Q390 92 468 40 V200 H0 Z" fill="var(--red-dark)"/>
      <path d="M0 96 Q120 76 250 86 Q390 98 468 48 V200 H0 Z" fill="var(--red)"/>
    </svg>

    <div class="abs pricing">
      <div class="pricing-label">Pricing</div>
      <div class="pricing-amount">$ 25 per participant</div>
      <div class="pricing-note">*Charged to Invoice post-show</div>
    </div>

    <div class="abs date-pill">Friday, August 17, 2018<br>at 1:00 p.m. – 2:00 p.m.</div>

    <div class="abs footer-brand">
      <span class="brand-dot"></span>
      <span class="brand-name">Birch Worldwide Solutions</span>
    </div>
    <p class="abs host white">Event is hosted by:&nbsp; Birch Worldwide Solutions<br>To Register for this Event, Go To:<br>https://www.tovrelin.example/bir18/fall/</p>

    <p class="abs questions white">Questions? For more information,</p>
    <p class="abs contact white">Contact: <strong>Martin Olsby</strong></p>
    <div class="abs contact-line phone white">
      <svg class="icon" viewBox="0 0 24 24"><circle cx="12" cy="12" r="10.5" fill="none" stroke="#fff" stroke-width="2"/><path d="M8 6.5l2 .2 1 3-1.4 1.2a8 8 0 0 0 3.5 3.5l1.2-1.4 3 1 .2 2c-.5 1-1.5 1.5-2.5 1.4C10 16.8 7.2 14 6.6 9c-.1-1 .4-2 1.4-2.5z" fill="#fff"/></svg>
      <span>555.014.2836</span>
    </div>
    <div class="abs contact-line email white">
      <svg class="icon" viewBox="0 0 24 24"><rect x="2" y="5" width="20" height="14" fill="none" stroke="#fff" stroke-width="2"/><path d="M2 6l10 7 10-7" fill="none" stroke="#fff" stroke-width="2"/></svg>
      <span>molsby@birchsupply.example</span>
    </div>
    <div class="abs contact-line web white">
      <svg class="icon" viewBox="0 0 24 24"><circle cx="12" cy="12" r="10" fill="none" stroke="#fff" stroke-width="2"/><ellipse cx="12" cy="12" rx="4.5" ry="10" fill="none" stroke="#fff" stroke-width="1.6"/><path d="M2 12h20" stroke="#fff" stroke-width="1.6"/></svg>
      <span>www.birchworldservicesgroup.example</span>
    </div>
  </main>
</body>
</html>
```